Business Card Design Project

I am community manager and social media strategist. I need a double sided business card with company logo and name. Looking for something professional, elegant but also a little bit original.

• - The logo and the colours are the company colours and a required to stay.
- The size should be: 84 x 55 mm (or 3.30 x 2.16)
- The file size should be: 1039 x 697 pixels (300 dpi)
- I'd like rounded corners. :)

Use the following contact information for the card:

Léonie Vardin
Stratégie médias sociaux / community management / édition de sites sociaux
mob. : 0687529103
leonie.vardin@postelune.fr
Twitter. : @lvardin
Skype : vardin.leonie

```html
<!DOCTYPE html>
<html lang="fr">
<head>
<meta charset="utf-8">
<title>NOVELIA – carte de visite recto verso</title>
<link rel="stylesheet" href="https://fonts.googleapis.com/css2?family=Noto+Sans:wght@400;700&display=swap">
<style>
  :root {
    --stage: #666666;
    --card-white: #ffffff;
    --brand-blue: #1b5c93;
    --brand-deep: #174d7c;
    --text-grey: #8f8f8f;
    --contact-grey: #7d7d7d;
    --sky: #1a8fd0;
    --ocean: #0b5a96;
    --night: #0a4a80;
  }
  * { margin: 0; padding: 0; box-sizing: border-box; }
  html, body {
    width: 1101px;
    height: 1200px;
    overflow: hidden;
    background: var(--stage);
    font-family: "Noto Sans", Verdana, sans-serif;
  }
  .sheet { position: relative; width: 1101px; height: 1200px; }

  .card {
    position: absolute;
    left: 134px;
    width: 738px;
    height: 482px;
    border-radius: 22px;
    overflow: hidden;
  }
  .card--front { top: 83px; background: var(--card-white); }
  .card--back { top: 650px; }

  /* front */
  .brand {
    position: absolute;
    display: flex;
    flex-direction: column;
    align-items: center;
  }
  .brand__dot {
    width: 118px;
    height: 118px;
    border-radius: 50%;
    background: var(--brand-blue);
  }
  .brand__name {
    font-weight: 700;
    letter-spacing: 2px;
    line-height: 1;
  }
  .card--front .brand { left: 55px; top: 60px; }
  .card--front .brand__name {
    margin-top: 22px;
    font-size: 42px;
    color: var(--brand-blue);
  }

  .contact {
    position: absolute;
    right: 63px;
    top: 57px;
    text-align: right;
    font-weight: 700;
    font-size: 21px;
    line-height: 25px;
  }
  .contact__mobile { color: var(--brand-deep); }
  .contact__email { color: var(--brand-blue); }
  .contact__social { color: var(--contact-grey); }
  .contact__icon {
    display: inline-block;
    width: 19px;
    height: 19px;
    margin-right: 6px;
    vertical-align: -2px;
    background: var(--sky);
  }
  .contact__icon--round { border-radius: 50%; }
  .contact__icon--square { border-radius: 3px; }

  .holder {
    position: absolute;
    left: 57px;
    top: 301px;
  }
  .holder__name {
    font-size: 26px;
    font-weight: 700;
    color: var(--brand-blue);
  }
  .holder__role {
    margin-top: 22px;
    font-size: 20px;
    font-weight: 700;
    line-height: 27px;
    color: var(--text-grey);
  }

  /* back */
  .back__waves {
    position: absolute;
    inset: 0;
    background:
      linear-gradient(160deg, rgba(40,170,230,0.55) 0%, rgba(40,170,230,0) 45%),
      linear-gradient(135deg, var(--sky) 0%, var(--ocean) 55%, var(--night) 100%);
  }
  .card--back .brand { left: 452px; top: 240px; }
  .card--back .brand__dot { background: var(--card-white); width: 104px; height: 104px; }
  .card--back .brand__name {
    margin-top: 22px;
    font-size: 44px;
    color: var(--card-white);
  }
</style>
</head>
<body>
<main class="sheet">
  <section class="card card--front" aria-label="Recto de la carte">
    <div class="brand">
      <span class="brand__dot"></span>
      <span class="brand__name">NOVELIA</span>
    </div>

    <address class="contact" style="font-style: normal;">
      <div class="contact__mobile">mob. : 0687529103</div>
      <div class="contact__email">leonie.vardin@postelune.fr</div>
      <div class="contact__social"><span class="contact__icon contact__icon--square"></span>@lvardin</div>
      <div class="contact__social"><span class="contact__icon contact__icon--round"></span>vardin.leonie</div>
    </address>

    <div class="holder">
      <h1 class="holder__name">Léonie Vardin</h1>
      <p class="holder__role">Stratégie médias sociaux / community<br>management / édition de sites sociaux</p>
    </div>
  </section>

  <section class="card card--back" aria-label="Verso de la carte">
    <div class="back__waves" role="img" aria-label="Fond bleu à vagues décoratives"></div>
    <div class="brand">
      <span class="brand__dot"></span>
      <span class="brand__name">NOVELIA</span>
    </div>
  </section>
</main>
</body>
</html>
```